I am a company selling interior designing materials

HI, I am selling interior design materials and require a namecard which is more outstanding while following a certain details placement as attached.

My clients are mainly interior designers so it has to attract their attention rather than feeling that its "just another namecard". I am selling wallcoverings, fabrics, acoustics and carpets.

Target Market(s)

interior designers designing hotels, commerical offices.

Contact Information for Business Card

As per attached.
Please change address to 47 Jalan 16 Tampines #05-02 Velmora Building Singapore 527314

Font styles to use
Other font styles liked:
• calibri

Requirements
Must have
• (1) company logo on top in the middle. Placement of contac details to be the same
• (2) company color is blue/green cymk 75/8/42/0
• (3) "KTV" logo to be prominent
• (4) You may change the logo but there should be a "swirl" surrounding the word KTV like current logo. The swirl pattern does not need to follow current logo and you may propose.
Should not have
• (1) there should not be any designs above "KTV" logo
• (2) no sharp triangles or angles

```html
<!DOCTYPE html>
<html lang="en">
<head>
<meta charset="utf-8">
<title>KTV Business Card</title>
<link rel="stylesheet" href="https://fonts.googleapis.com/css2?family=Montserrat:wght@500;600;700;800&display=swap">
<style>
  :root {
    --bg: #ececec;
    --card-grey: #6b6867;
    --brand-teal: #2ba59e;
    --paper: #ffffff;
    --paper-tint: #f2f2f2;
    --text-light: #f4f4f4;
  }
  * { margin: 0; padding: 0; box-sizing: border-box; }
  html, body {
    width: 1200px; height: 1175px; overflow: hidden;
    background: var(--bg);
    font-family: "Montserrat", Arial, sans-serif;
  }
  .card {
    position: absolute; left: 150px;
    width: 900px; height: 515px;
    overflow: hidden;
    box-shadow: 0 6px 18px rgba(0,0,0,0.12);
  }
  .card--front { top: 40px; background: var(--card-grey); }
  .card--back  { top: 615px; background: var(--card-grey); }
  .card__shape { position: absolute; inset: 0; }

  .brand {
    position: absolute; left: 20px; top: 110px; width: 520px;
    text-align: center; color: var(--card-grey);
  }
  .brand__name {
    font-size: 130px; font-weight: 800; line-height: 1; letter-spacing: 4px;
  }
  .brand__company {
    margin-top: 22px; font-size: 20px; font-weight: 700;
  }

  .contact {
    position: absolute; left: 605px; top: 180px; width: 285px;
    color: var(--text-light); white-space: nowrap;
  }
  .contact__name { font-size: 32px; font-weight: 800; }
  .contact__mobile { font-size: 17px; font-weight: 600; margin-top: 6px; }
  .contact__rule {
    width: 40px; height: 2px; background: var(--text-light);
    opacity: 0.6; margin: 20px 0 18px;
  }
  .contact__line { font-size: 15.5px; font-weight: 500; line-height: 1.6; }

  .back-brand {
    position: absolute; inset: 0;
    display: flex; flex-direction: column; align-items: center; justify-content: center;
    color: var(--paper-tint);
  }
  .back-brand__name {
    font-size: 170px; font-weight: 800; line-height: 1; letter-spacing: 6px;
  }
  .back-brand__services {
    margin-top: 40px; font-size: 26px; font-weight: 700; letter-spacing: 1px;
  }
</style>
</head>
<body>

<section class="card card--front">
  <svg class="card__shape" width="900" height="515" viewBox="0 0 900 515">
    <path d="M0 0 L560 0 C640 120 560 380 290 515 L0 515 Z" fill="var(--paper)"/>
    <path d="M560 0 C640 120 560 380 290 515" fill="none" stroke="var(--brand-teal)" stroke-width="12"/>
  </svg>
  <div class="brand">
    <div class="brand__name">KTV</div>
    <div class="brand__company">KaTaVi InteriorFurnishings Pte Ltd</div>
  </div>
  <div class="contact">
    <div class="contact__name">Lorna TAN</div>
    <div class="contact__mobile">(65) 9172 4053</div>
    <div class="contact__rule"></div>
    <div class="contact__line">(65) 6281 7420</div>
    <div class="contact__line">lorna@ktvfurnishings.com</div>
    <div class="contact__line">47 Jalan 16 Tampines #05-02</div>
    <div class="contact__line">Velmora Building Singapore 527314</div>
  </div>
</section>

<section class="card card--back">
  <div class="back-brand">
    <div class="back-brand__name">KTV</div>
    <div class="back-brand__services">Wallcoverings • Acoustic • Fabrics • Carpet</div>
  </div>
</section>

</body>
</html>
```